First time author needs a cover design for both eBook and print.

We are looking for a book cover for an adventure / memoir / narrative non-fiction book.

The title of the book is "Harrowgate to Salerno: Where's the catch?" - Part One. The Authors name is "Desmond Hargrove Tulliver". The book cover is standard size 5.5"x8.5", along with the Back Cover. Standard spine size.

---------------------------------------------------------------------

The Book Summary is as follows:

The first of a series, the story begins near Pittsburgh, PA, and takes the protagonist and his friend to N.Y.C. where the two buy one-way tickets to Europe. Landing in Luxembourg, they stop in Amsterdam for a couple days, and then travel to Manchester, England. A short adventure, they are then driven to the Highlands of Scotland for real purpose. Contracted to harvest Christmas trees, the protagonist battles with his traveling partner, the weather, the locals, and his penchant for drugs and alcohol. He’s searching for the difference to things and the real meaning of art.

The year is 1998.

The picture attached is of the protagonist getting his picture taken as he focuses his camera. In the background the van he got a ride to work in is engulfed with flames. A discarded roach was the catalyst. Scottish Highlands.

The final design should incorporate the picture provided to set a tone of intrigue, with a matte, classic/literature finish similar to those of that era. With or without the van burning. You can redraw the image for more impact or use it in your design.

Back cover: Not too long ago there was still some mystery in life. It was as if the outside world was actually interesting. There were foreign lands to discover, beautiful women, new languages … life was exciting. Now it’s a little different. Everything is at hand: indisputable knowledge, social media, free porn, cameras in our phones, and the avoidable reality that there are too many of us and it’s getting hotter. 1998 was a lot different. Life was so simple then.

Also use the provided publishing logo for the spine.

Target readers are between 19 and 49, adventure/memoir/narrative nonfiction.

Target Market(s)

Font styles to use
Serif
Script

Colors
000000
0bac94
a6cf38
33a6d7
fbee3e

Requirements
Must have
• The final design should incorporate the picture provided which contains a photo of the actual author of the memoir. The picture attached is of the protagonist getting his picture taken as he focuses his camera. In the background the van he got a ride to work in is engulfed with flames. A discarded roach was the catalyst. Scottish Highlands pine forests is also included.
• The final design should incorporate the picture provided to set a tone of intrigue, with a matte, classic/literature finish similar to those of that era. With or without the van burning. You can redraw the image for more impact or use it in your design.
Nice to have
• Literary feel like Past the Bend, Under the Ridge, Dread and Mischief at Shallow Creek.
Should not have
• Should not be glossy or cheesy looking

```html
<!DOCTYPE html>
<html lang="en">
<head>
<meta charset="utf-8">
<title>Harrowgate to Salerno: Where's the catch? — Cover Wrap</title>
<link rel="stylesheet" href="https://fonts.googleapis.com/css2?family=Barlow+Condensed:wght@500;600&family=Yellowtail&family=Lilita+One&display=swap">
<style>
  :root {
    --bg: #e4e4e4;
    --paper: #f1f2f6;
    --paper-cool: #dfe1ea;
    --ink: #1a1a1a;
    --title-green: #2f6b52;
    --title-yellow: #f2e13c;
    --title-blue: #33a6d7;
    --publisher-blue: #2c4f9a;
    --strip-top: #6f7196;
    --strip-bottom: #4b4d79;
    --photo-sky: #b9bdd6;
    --photo-hill: #a88a55;
    --photo-ground: #5f5236;
  }
  * { box-sizing: border-box; margin: 0; padding: 0; }
  html, body { width: 1200px; height: 908px; overflow: hidden; background: var(--bg); }
  .wrap {
    position: absolute; left: 47px; top: 54px;
    width: 1106px; height: 800px;
    display: flex;
    box-shadow: 0 6px 18px rgba(0,0,0,.18);
  }

  /* Back cover */
  .back {
    position: relative; width: 518px; height: 100%;
    background: linear-gradient(90deg, var(--paper-cool) 0%, var(--paper) 60%);
    overflow: hidden;
  }
  .back-strip {
    position: absolute; left: 0; top: 0; width: 120px; height: 100%;
    background:
      linear-gradient(90deg, rgba(241,242,246,0) 55%, var(--paper-cool) 100%),
      linear-gradient(180deg, var(--strip-top), var(--strip-bottom) 45%, var(--strip-top) 100%);
  }
  .blurb {
    position: absolute; left: 150px; top: 300px; width: 240px;
    font-family: "Barlow Condensed", sans-serif; font-weight: 500;
    font-size: 15.5px; line-height: 1.3; color: var(--ink);
  }
  .blurb p + p { margin-top: 2px; }
  .back-publisher {
    position: absolute; left: 300px; top: 650px;
    font-family: "Barlow Condensed", sans-serif; font-weight: 600;
    font-size: 18px; color: var(--publisher-blue);
    display: flex; align-items: center; gap: 6px;
  }
  .back-publisher .dot { width: 10px; height: 10px; border-radius: 50%; background: var(--publisher-blue); }
  .price-box {
    position: absolute; left: 310px; top: 690px; width: 160px; height: 80px;
    background: #fff; border: 1px solid #333;
  }

  /* Spine */
  .spine {
    position: relative; width: 70px; height: 100%;
    background: linear-gradient(90deg, #cfd1da, var(--paper) 40%, #e6e7ee);
    display: flex; flex-direction: column; align-items: center;
    padding: 18px 0 20px;
  }
  .spine-title {
    writing-mode: vertical-rl;
    font-family: "Barlow Condensed", sans-serif; font-weight: 600;
    font-size: 25px; color: var(--ink); white-space: nowrap;
  }
  .spine-publisher {
    margin-top: 22px; writing-mode: vertical-rl;
    font-family: "Barlow Condensed", sans-serif; font-weight: 600;
    font-size: 13px; color: var(--publisher-blue); white-space: nowrap;
  }
  .spine-author {
    margin-top: auto; writing-mode: vertical-rl;
    font-family: "Barlow Condensed", sans-serif; font-weight: 500;
    font-size: 19px; color: var(--ink); white-space: nowrap;
  }

  /* Front cover */
  .front {
    position: relative; width: 518px; height: 100%;
    background: var(--paper); overflow: hidden;
  }
  .cover-photo {
    position: absolute; left: 0; right: 0; bottom: 0; height: 420px;
    background: linear-gradient(180deg,
      var(--paper) 0%,
      var(--photo-sky) 18%,
      var(--photo-hill) 48%,
      var(--photo-ground) 100%);
  }
  .front-author {
    position: absolute; top: 34px; left: 0; right: 0; text-align: center;
    font-family: "Barlow Condensed", sans-serif; font-weight: 500;
    font-size: 32px; color: var(--ink);
  }
  .title-script {
    position: absolute; left: 26px; top: 150px; width: 450px;
    font-family: "Yellowtail", cursive; font-weight: 400;
    color: var(--title-green);
    transform: rotate(-6deg); transform-origin: left top;
    line-height: 1;
  }
  .title-script .line1 { display: block; font-size: 60px; white-space: nowrap; }
  .title-script .joiner { font-size: 26px; vertical-align: 26px; margin-left: 6px; }
  .title-script .line2 { display: block; font-size: 60px; text-align: right; padding-right: 10px; white-space: nowrap; }
  .subtitle {
    position: absolute; left: 24px; top: 300px; width: 440px;
    font-family: "Lilita One", sans-serif; font-weight: 400;
    font-size: 60px; line-height: .95;
    color: var(--title-yellow);
    -webkit-text-stroke: 2px var(--title-blue);
    paint-order: stroke fill;
    transform: rotate(-8deg); transform-origin: left top;
  }
  .subtitle span { display: block; white-space: nowrap; }
  .subtitle span + span { padding-left: 30px; }
</style>
</head>
<body>
  <main class="wrap">
    <section class="back">
      <div class="back-strip" role="img" aria-label="Landscape photograph of a misty shoreline and tree line"></div>
      <div class="blurb">
        <p>Not too long ago there was still some mystery in life. It was as if the outside world was actually interesting. There were foreign lands to discover, beautiful women, new languages …life was exciting.</p>
        <p>Now it's a little different. Everything is at hand: indisputable knowledge, social media, free porn, cameras in our phones, and the avoidable reality that there are too many of us and it's getting hotter. 1998 was a lot different. Life was so simple then.</p>
      </div>
      <div class="back-publisher"><span class="dot"></span>Tallgrass Row Publishing</div>
      <div class="price-box"></div>
    </section>

    <section class="spine">
      <div class="spine-title">Harrowgate to Salerno: Where's the catch?</div>
      <div class="spine-publisher">Tallgrass Row Publishing</div>
      <div class="spine-author">Desmond Hargrove Tulliver</div>
    </section>

    <section class="front">
      <div class="cover-photo" role="img" aria-label="Photograph of a man taking a picture on a Highland hillside, a van burning behind him"></div>
      <div class="front-author">Desmond Hargrove Tulliver</div>
      <h1 class="title-script">
        <span class="line1">Harrowgate<span class="joiner">to</span></span>
        <span class="line2">Salerno</span>
      </h1>
      <h2 class="subtitle"><span>Where's</span><span>the catch?</span></h2>
    </section>
  </main>
</body>
</html>
```